7 P's for Healthcare Companies - Textbook Graphic

Can you create a graphic for me for a medical textbook? The goal is to show 7 critical features of a healthcare startup and the audience is physicians with limited business backgrounds.

Please include a picture of young, male emergency physician in the middle of the graphic. Show them evaluating an idea. Can you surround the physician with bold writing for the seven components, and use brief descriptions and simple images or graphics to illustrate the point?

The image should be somewhat formal, but it's OK to be lighthearded.

The seven P's and brief descriptions include the following:
Product: what is their market solution?
(Intellectual) Property: do they have a patent or trademark?
Product Clearance: how will they get QRB approval and TPW clearance?
Payment: how will they make money?
Pilots: have they applied their product in a healthcare setting?
Physician and Patient feedback: Do doctors and patients like their product?
Publication: do they have evidence their product works?

More detail and information is available at this website: https://brenvolt.com/blog/uncategorized/healthcare-framework/

I will need to own this image

```html
<!DOCTYPE html>
<html lang="en">
<head>
<meta charset="utf-8">
<title>7 P's for Healthcare Companies</title>
<link rel="stylesheet" href="https://fonts.googleapis.com/css2?family=Arimo:wght@400;700&display=swap">
<style>
  :root {
    --backdrop: #b5b5b5;
    --page: #ffffff;
    --header: #474645;
    --ink: #111111;
    --product: #f15a22;
    --property: #4a8a3f;
    --clearance: #34c6f1;
    --payment: #3150a2;
    --pilots: #7f5ba8;
    --feedback: #c4588a;
    --publication: #7a8fa3;
    --portrait-light: #e39a9c;
    --portrait-dark: #d4878a;
    --hub-ring: #3e3e3e;
    --icon-shadow: #3a3a3a;
  }
  html, body {
    margin: 0;
    width: 1200px;
    height: 1200px;
    overflow: hidden;
    background: var(--backdrop);
  }
  .poster {
    position: absolute;
    left: 172px;
    top: 0;
    width: 856px;
    height: 1200px;
    display: block;
  }
  .poster text { font-family: "Arimo", Arial, sans-serif; }
  .header-band { fill: var(--header); }
  .header-title { fill: #fff; font-weight: 700; font-size: 142px; text-anchor: middle; }
  .header-subtitle { fill: #fff; font-weight: 700; font-size: 70px; text-anchor: middle; }
  .sector-outline { fill: var(--page); stroke-width: 2; }
  .step-title { fill: var(--ink); font-weight: 700; font-size: 24px; text-anchor: middle; }
  .step-text { fill: var(--ink); font-weight: 400; font-size: 23.5px; text-anchor: middle; }
  .icon-halo { fill: var(--page); stroke-width: 2.5; }
  .icon-shadow { fill: var(--icon-shadow); opacity: .75; }
  .icon-face { fill: #f4f4f4; }
  .hub-ring { fill: none; stroke: var(--hub-ring); stroke-width: 9; }
</style>
</head>
<body>
<svg class="poster" viewBox="0 0 1192 1672" xmlns="http://www.w3.org/2000/svg">
  <defs>
    <radialGradient id="portrait-tone" cx="50%" cy="45%" r="60%">
      <stop offset="0" stop-color="var(--portrait-light)"/>
      <stop offset="1" stop-color="var(--portrait-dark)"/>
    </radialGradient>
  </defs>

  <rect width="1192" height="1672" fill="var(--page)"/>

  <!-- Header -->
  <rect class="header-band" width="1192" height="273"/>
  <text class="header-title" x="582" y="145">7 P's</text>
  <text class="header-subtitle" x="582" y="228">for Healthcare Companies</text>

  <!-- Sector outlines -->
  <g class="sectors">
    <path class="sector-outline" stroke="var(--product)" d="M603.4 738.1 L610.8 525.3 A425 425 0 0 1 918.9 673.7 L757.1 812.2 A212 212 0 0 0 603.4 738.1 Z"/>
    <path class="sector-outline" stroke="var(--property)" d="M766.3 823.7 L937.3 696.8 A425 425 0 0 1 1013.4 1030.1 L804.2 989.9 A212 212 0 0 0 766.3 823.7 Z"/>
    <path class="sector-outline" stroke="var(--clearance)" d="M800.9 1004.4 L1006.8 1059.0 A425 425 0 0 1 793.7 1326.3 L694.6 1137.7 A212 212 0 0 0 800.9 1004.4 Z"/>
    <path class="sector-outline" stroke="var(--payment)" d="M681.2 1144.1 L766.9 1339.1 A425 425 0 0 1 425.1 1339.1 L510.8 1144.1 A212 212 0 0 0 681.2 1144.1 Z"/>
    <path class="sector-outline" stroke="var(--pilots)" d="M497.4 1137.7 L398.3 1326.3 A425 425 0 0 1 185.2 1059.0 L391.1 1004.4 A212 212 0 0 0 497.4 1137.7 Z"/>
    <path class="sector-outline" stroke="var(--feedback)" d="M387.8 989.9 L178.6 1030.1 A425 425 0 0 1 254.7 696.8 L425.7 823.7 A212 212 0 0 0 387.8 989.9 Z"/>
    <path class="sector-outline" stroke="var(--publication)" d="M434.9 812.2 L273.1 673.7 A425 425 0 0 1 581.2 525.3 L588.6 738.1 A212 212 0 0 0 434.9 812.2 Z"/>
  </g>

  <!-- Ring bands -->
  <g class="ring-bands">
    <path fill="var(--product)" d="M612.8 470.3 A480 480 0 0 1 960.7 637.9 L918.9 673.7 A425 425 0 0 0 610.8 525.3 Z"/>
    <path fill="var(--property)" d="M981.5 664.0 A480 480 0 0 1 1067.4 1040.4 L1013.4 1030.1 A425 425 0 0 0 937.3 696.8 Z"/>
    <path fill="var(--clearance)" d="M1060.0 1073.1 A480 480 0 0 1 819.2 1374.9 L793.7 1326.3 A425 425 0 0 0 1006.8 1059.0 Z"/>
    <path fill="var(--payment)" d="M789.0 1389.5 A480 480 0 0 1 403.0 1389.5 L425.1 1339.1 A425 425 0 0 0 766.9 1339.1 Z"/>
    <path fill="var(--pilots)" d="M372.8 1374.9 A480 480 0 0 1 132.0 1073.1 L185.2 1059.0 A425 425 0 0 0 398.3 1326.3 Z"/>
    <path fill="var(--feedback)" d="M124.6 1040.4 A480 480 0 0 1 210.5 664.0 L254.7 696.8 A425 425 0 0 0 178.6 1030.1 Z"/>
    <path fill="var(--publication)" d="M231.3 637.9 A480 480 0 0 1 579.2 470.3 L581.2 525.3 A425 425 0 0 0 273.1 673.7 Z"/>
  </g>

  <!-- Central portrait area -->
  <g class="hub">
    <circle cx="596" cy="950" r="198" fill="url(#portrait-tone)" role="img" aria-label="Illustration of a young male emergency physician holding a clipboard and looking at a glowing light bulb idea in his hand"/>
    <circle class="hub-ring" cx="596" cy="950" r="198"/>
  </g>

  <!-- Step icons -->
  <g class="step-icon">
    <circle class="icon-halo" stroke="var(--product)" cx="800" cy="520" r="82"/>
    <circle fill="var(--product)" cx="800" cy="520" r="70"/>
    <circle class="icon-shadow" cx="808" cy="528" r="40"/>
    <circle class="icon-face" cx="800" cy="520" r="40"/>
    <circle fill="var(--product)" cx="800" cy="520" r="24"/>
    <path d="M789 520 l8 8 l14 -15" fill="none" stroke="#fff" stroke-width="4" stroke-linecap="round" stroke-linejoin="round"/>
  </g>
  <g class="step-icon">
    <circle class="icon-halo" stroke="var(--property)" cx="1064" cy="843" r="82"/>
    <circle fill="var(--property)" cx="1064" cy="843" r="70"/>
    <circle class="icon-shadow" cx="1072" cy="851" r="40"/>
    <circle class="icon-face" cx="1064" cy="843" r="40"/>
    <path d="M1055 855 v18 l9 -6 l9 6 v-18" fill="var(--property)"/>
    <circle cx="1064" cy="833" r="21" fill="none" stroke="var(--property)" stroke-width="5"/>
    <circle cx="1064" cy="833" r="10" fill="none" stroke="var(--property)" stroke-width="3"/>
  </g>
  <g class="step-icon">
    <circle class="icon-halo" stroke="var(--clearance)" cx="973" cy="1251" r="82"/>
    <circle fill="var(--clearance)" cx="973" cy="1251" r="70"/>
    <circle class="icon-shadow" cx="981" cy="1259" r="40"/>
    <circle class="icon-face" cx="973" cy="1251" r="40"/>
    <path d="M962 1226 h17 l10 10 v30 h-27 Z" fill="var(--clearance)"/>
    <path d="M970 1242 h13 M970 1250 h13 M970 1258 h13" stroke="#fff" stroke-width="2.5"/>
    <circle cx="960" cy="1262" r="11" fill="var(--clearance)" stroke="#fff" stroke-width="2"/>
    <path d="M955 1262 l4 4 l7 -7" fill="none" stroke="#fff" stroke-width="2.5"/>
  </g>
  <g class="step-icon">
    <circle class="icon-halo" stroke="var(--payment)" cx="596" cy="1431" r="82"/>
    <circle fill="var(--payment)" cx="596" cy="1431" r="70"/>
    <circle class="icon-shadow" cx="604" cy="1439" r="40"/>
    <circle class="icon-face" cx="596" cy="1431" r="40"/>
    <rect x="586" y="1408" width="32" height="18" rx="2" fill="none" stroke="var(--payment)" stroke-width="4" transform="rotate(-12 602 1417)"/>
    <circle cx="602" cy="1417" r="4" fill="var(--payment)"/>
    <rect x="568" y="1432" width="8" height="20" fill="var(--payment)"/>
    <path d="M579 1436 h14 l12 -4 c6 -1 8 4 4 6 l-16 12 h-14 Z" fill="var(--payment)"/>
  </g>
  <g class="step-icon">
    <circle class="icon-halo" stroke="var(--pilots)" cx="222" cy="1251" r="82"/>
    <circle fill="var(--pilots)" cx="222" cy="1251" r="70"/>
    <circle class="icon-shadow" cx="230" cy="1259" r="40"/>
    <circle class="icon-face" cx="222" cy="1251" r="40"/>
    <path d="M222 1248 c-14 -10 -16 -22 -8 -26 c4 -2 7 0 8 3 c1 -3 4 -5 8 -3 c8 4 6 16 -8 26 Z" fill="var(--pilots)"/>
    <path d="M222 1228 v10 M217 1233 h10" stroke="#fff" stroke-width="2.5"/>
    <path d="M198 1236 c-2 14 6 22 16 28 v8 M246 1236 c2 14 -6 22 -16 28 v8" fill="none" stroke="var(--pilots)" stroke-width="5" stroke-linecap="round"/>
  </g>
  <g class="step-icon">
    <circle class="icon-halo" stroke="var(--feedback)" cx="128" cy="843" r="82"/>
    <circle fill="var(--feedback)" cx="128" cy="843" r="70"/>
    <circle class="icon-shadow" cx="136" cy="851" r="40"/>
    <circle class="icon-face" cx="128" cy="843" r="40"/>
    <path d="M110 818 v10 c0 7 12 7 12 0 v-10 M116 835 v6 c0 4 6 4 10 2" fill="none" stroke="var(--feedback)" stroke-width="3.5"/>
    <circle cx="142" cy="828" r="4" fill="none" stroke="var(--feedback)" stroke-width="3"/>
    <rect x="100" y="847" width="56" height="18" rx="3" fill="var(--feedback)"/>
    <path d="M112 851 l1.5 4 h4 l-3.3 2.4 1.2 4 -3.4 -2.5 -3.4 2.5 1.2 -4 -3.3 -2.4 h4 Z M128 851 l1.5 4 h4 l-3.3 2.4 1.2 4 -3.4 -2.5 -3.4 2.5 1.2 -4 -3.3 -2.4 h4 Z M144 851 l1.5 4 h4 l-3.3 2.4 1.2 4 -3.4 -2.5 -3.4 2.5 1.2 -4 -3.3 -2.4 h4 Z" fill="#fff"/>
  </g>
  <g class="step-icon">
    <circle class="icon-halo" stroke="var(--publication)" cx="387" cy="520" r="82"/>
    <circle fill="var(--publication)" cx="387" cy="520" r="70"/>
    <circle class="icon-shadow" cx="395" cy="528" r="40"/>
    <circle class="icon-face" cx="387" cy="520" r="40"/>
    <path d="M380 493 h22 l6 6 v34 h-8" fill="none" stroke="var(--publication)" stroke-width="3"/>
    <rect x="366" y="500" width="30" height="38" fill="var(--publication)"/>
    <path d="M371 508 h20 M371 514 h20 M371 520 h20 M371 526 h20 M371 532 h14" stroke="#fff" stroke-width="2"/>
  </g>

  <!-- Step text -->
  <g class="step-copy">
    <text class="step-title" x="455" y="646">Publication:</text>
    <text class="step-text" x="455" y="679">Do they have evidence</text>
    <text class="step-text" x="455" y="708">their product works?</text>

    <text class="step-title" x="735" y="646">Product:</text>
    <text class="step-text" x="735" y="679">What is their</text>
    <text class="step-text" x="735" y="708">market solution?</text>

    <text class="step-title" x="898" y="840">(Intellectual)</text>
    <text class="step-title" x="898" y="868">Property:</text>
    <text class="step-text" x="898" y="904">Do they have a</text>
    <text class="step-text" x="898" y="933">patent or</text>
    <text class="step-text" x="898" y="962">trademark?</text>

    <text class="step-title" x="828" y="1090">Product</text>
    <text class="step-title" x="828" y="1118">Clearance:</text>
    <text class="step-text" x="828" y="1155">How will they get</text>
    <text class="step-text" x="828" y="1184">QRB approval</text>
    <text class="step-text" x="828" y="1213">and TPW</text>
    <text class="step-text" x="828" y="1242">clearance?</text>

    <text class="step-title" x="593" y="1230">Payment:</text>
    <text class="step-text" x="593" y="1268">How will they</text>
    <text class="step-text" x="593" y="1297">make money?</text>

    <text class="step-title" x="362" y="1092">Pilots:</text>
    <text class="step-text" x="362" y="1128">Have they</text>
    <text class="step-text" x="362" y="1157">applied their product</text>
    <text class="step-text" x="362" y="1186">in a</text>
    <text class="step-text" x="362" y="1215">healthcare</text>
    <text class="step-text" x="362" y="1244">setting?</text>

    <text class="step-title" x="298" y="824">Physician and</text>
    <text class="step-title" x="298" y="852">Patient</text>
    <text class="step-title" x="298" y="880">feedback:</text>
    <text class="step-text" x="298" y="914">Do doctors and</text>
    <text class="step-text" x="298" y="943">patients like</text>
    <text class="step-text" x="298" y="972">their product?</text>
  </g>
</svg>
</body>
</html>
```